Lip Balm Product Box (Eco Friendly & Eco Elegant)

Full Redesign
I am looking to upgrade my style and make it more eco-elegant

I am seeking a packaging redesign to elevate my brand and product in the mind of the consumer. The branding inspiration that I am going for is the simplicity of Oud Miret meets the styling of Rosalind Pemworth.

I would like to elevate my brand to become the eco-friendly Vestrom

The new packaging can include a cutout so the product is visible.

All text is optional and changeable.

What is your vision?

Target Market(s)

Female & Male age 18-26 in need of support and encouragement. Our brand users believe in the reduction of single use plastics are positive affirmations.

Industry/Entity Type

Cosmetics and body care products

Font styles to use
Serif
Decorative

Colors

Designer to choose colors to be used in the design.

Requirements
Must have
• A reference to "Plastic free"

```html
<!DOCTYPE html>
<html lang="en">
<head>
<meta charset="utf-8">
<title>Veldra Body Care – Lip &amp; Body Balm Box Dieline</title>
<link href="https://fonts.googleapis.com/css2?family=Cardo:wght@400&display=swap" rel="stylesheet">
<style>
  :root{
    --paper:#ffffff;
    --board:#231f20;
    --gold:#b0862f;
    --ink:#231f20;
    --crease:#d9d9d9;
  }
  html,body{margin:0;padding:0;width:1200px;height:1200px;overflow:hidden;background:var(--paper);}
  .dieline{display:block;width:1200px;height:1200px;}
  .board{fill:var(--board);}
  .crease{fill:none;stroke:var(--crease);stroke-width:0.8;}
  .panel{fill:var(--gold);}
  .window{fill:none;stroke:var(--ink);stroke-width:1;}
  .copy{font-family:'Cardo',serif;fill:var(--ink);text-anchor:middle;}
  .brand{font-size:34px;}
  .brand-sm{font-size:25px;}
  .brand-sub{font-size:14px;}
  .brand-sub-sm{font-size:11px;}
  .web{font-size:11px;}
  .claim{font-size:12px;letter-spacing:1px;}
  .product-name{font-size:22px;}
  .panel-title{font-size:23px;}
  .body-copy{font-size:16.5px;}
  .fine-print{font-size:13px;}
</style>
</head>
<body>
<svg class="dieline" viewBox="420 20 1090 1320" xmlns="http://www.w3.org/2000/svg" role="img" aria-label="Flat dieline of the Veldra lip and body balm box">
  <!-- top tuck flap and top panel -->
  <path class="board" d="M526 165 V75 Q526 25 576 25 H712 Q762 25 762 75 V165 Z"/>
  <path class="crease" d="M530 150 V80 Q530 30 578 30 H710 Q757 30 757 80 V150 H700 V160 H588 V150 Z"/>
  <rect class="board" x="526" y="160" width="236" height="225"/>
  <rect class="panel" x="536" y="170" width="216" height="202"/>
  <g class="brand-name">
    <text class="copy brand" x="642" y="266">Veldra</text>
    <text class="copy brand-sub" x="642" y="286">Body Care</text>
  </g>
  <text class="copy web" x="642" y="335">www.VeldraBodyCare.com</text>
  <text class="copy claim" x="642" y="357">PLASTIC FREE</text>

  <!-- side dust flaps, top -->
  <path class="board" d="M762 273 H998 V387 H762 Z"/>
  <path class="crease" d="M800 275 L792 350 L768 380 M948 275 L965 345 L993 380"/>
  <path class="board" d="M1228 273 H1465 V387 H1228 Z"/>
  <path class="crease" d="M1285 275 L1275 348 L1240 385 M1430 275 L1440 350 L1462 385"/>

  <!-- main body strip -->
  <polygon class="board" points="468,382 526,382 526,972 468,972"/>
  <path class="crease" d="M470 385 L524 395 V960 L470 970"/>
  <rect class="board" x="526" y="382" width="939" height="590"/>
  <path class="crease" d="M526 382 H1465 M526 972 H1465 M762 382 V972 M998 382 V972 M1235 382 V972"/>

  <!-- front panel -->
  <rect class="panel" x="536" y="392" width="216" height="570"/>
  <g class="brand-name">
    <text class="copy brand-sm" x="640" y="447">Veldra</text>
    <text class="copy brand-sub-sm" x="640" y="463">Body Care</text>
  </g>
  <rect class="window" x="556" y="495" width="175" height="363"/>
  <text class="copy product-name" x="644" y="903">All Purpose</text>
  <text class="copy product-name" x="644" y="929">Lip &amp; Body Balm</text>

  <!-- english side panel -->
  <rect class="panel" x="772" y="397" width="216" height="565"/>
  <text class="copy panel-title" x="879" y="442">Veldra Body Care</text>
  <text class="copy body-copy" x="879" y="478">
    <tspan x="879">Veldra was created to</tspan>
    <tspan x="879" dy="18">give a little lift to your</tspan>
    <tspan x="879" dy="18">emotional well-being by</tspan>
    <tspan x="879" dy="18">inspiring positivity and</tspan>
    <tspan x="879" dy="18">offering encouragement.</tspan>
    <tspan x="879" dy="18">Veldra’s messages remind</tspan>
    <tspan x="879" dy="18">us that we can do</tspan>
    <tspan x="879" dy="18">anything and be our</tspan>
    <tspan x="879" dy="18">best selves</tspan>
    <tspan x="879" dy="36">Support</tspan>
    <tspan x="879" dy="18">A portion of each sale</tspan>
    <tspan x="879" dy="18">is used to help at risk</tspan>
    <tspan x="879" dy="18">people around the</tspan>
    <tspan x="879" dy="18">world.</tspan>
    <tspan x="879" dy="36">Ingredients</tspan>
    <tspan x="879" dy="18">Soybean Seed Oil</tspan>
    <tspan x="879" dy="18">Beeswax</tspan>
    <tspan x="879" dy="18">Sunflower Seed Oil</tspan>
    <tspan x="879" dy="18">Shea Butter</tspan>
    <tspan x="879" dy="18">Cocoa Butter</tspan>
    <tspan x="879" dy="18">Vitamin E</tspan>
    <tspan x="879" dy="18">Aloe Leaf</tspan>
  </text>

  <!-- back panel -->
  <rect class="panel" x="1008" y="397" width="217" height="565"/>
  <g class="brand-name">
    <text class="copy brand-sm" x="1113" y="447">Veldra</text>
    <text class="copy brand-sub-sm" x="1113" y="463">Body Care</text>
  </g>
  <rect class="window" x="1030" y="498" width="173" height="364"/>
  <text class="copy product-name" x="1117" y="906">Baume à Lèvres</text>
  <text class="copy product-name" x="1117" y="932">Naturel</text>

  <!-- french side panel -->
  <rect class="panel" x="1245" y="397" width="210" height="565"/>
  <text class="copy panel-title" x="1350" y="442" style="font-size:21px">Soins du corps Veldra</text>
  <text class="copy body-copy" x="1350" y="467">
    <tspan x="1350">Veldra a été conçu pour</tspan>
    <tspan x="1350" dy="16.3">donner un petit coup de</tspan>
    <tspan x="1350" dy="16.3">pouce à l'état</tspan>
    <tspan x="1350" dy="16.3">émotionnel d'une</tspan>
    <tspan x="1350" dy="16.3">personne en utilisant la</tspan>
    <tspan x="1350" dy="16.3">positivité et</tspan>
    <tspan x="1350" dy="16.3">l'encouragement. Il</tspan>
    <tspan x="1350" dy="16.3">contient un message de</tspan>
    <tspan x="1350" dy="16.3">motivation qui nous</tspan>
    <tspan x="1350" dy="16.3">rappelle que nous</tspan>
    <tspan x="1350" dy="16.3">pouvons tout faire et</tspan>
    <tspan x="1350" dy="16.3">être n'importe qui.</tspan>
    <tspan x="1350" dy="28">Soutien</tspan>
    <tspan x="1350" dy="31">Une portion de chaque</tspan>
    <tspan x="1350" dy="16.3">vente sera attribuée à</tspan>
    <tspan x="1350" dy="16.3">des organismes venant</tspan>
    <tspan x="1350" dy="16.3">en aide aux personnes</tspan>
    <tspan x="1350" dy="16.3">en difficulté dans le</tspan>
    <tspan x="1350" dy="16.3">monde entier.</tspan>
    <tspan x="1350" dy="28">Ingrédients</tspan>
    <tspan x="1350" dy="24">Huile de soja</tspan>
    <tspan x="1350" dy="16.3">Cire d'abeille</tspan>
    <tspan x="1350" dy="16.3">Huile de tournesol</tspan>
    <tspan x="1350" dy="16.3">Beurre de karité</tspan>
    <tspan x="1350" dy="16.3">Beurre de cacao</tspan>
    <tspan x="1350" dy="16.3">Vitamine E</tspan>
    <tspan x="1350" dy="16.3">Feuille d'aloès</tspan>
  </text>

  <!-- side dust flaps, bottom -->
  <rect class="board" x="762" y="972" width="236" height="113"/>
  <path class="crease" d="M768 975 L795 1015 L802 1082 M993 975 L968 1020 L960 1082"/>
  <rect class="board" x="1235" y="972" width="230" height="113"/>
  <path class="crease" d="M1240 975 L1270 1015 L1278 1082 M1462 975 L1435 1020 L1428 1082"/>

  <!-- bottom panel and tuck flap -->
  <rect class="board" x="998" y="972" width="237" height="238"/>
  <rect class="panel" x="1008" y="985" width="217" height="205"/>
  <text class="copy fine-print" x="1117" y="1005">
    <tspan x="1117">Ingredients:</tspan>
    <tspan x="1117" dy="17">Glycine Soja (Soybean)</tspan>
    <tspan x="1117" dy="17">Oil, Beeswax, Helianthus Annuus</tspan>
    <tspan x="1117" dy="17">(Sunflower) Seed Oil, Theobroma</tspan>
    <tspan x="1117" dy="17">Cacao (Cocoa) Seed Butter,</tspan>
    <tspan x="1117" dy="17">Butyrospermum Parkii (Shea</tspan>
    <tspan x="1117" dy="17">Butter) Fruit, Tocopherol Acetate,</tspan>
    <tspan x="1117" dy="17">Aloe Barbadensis Leaf Juice.</tspan>
    <tspan x="1117" dy="23">Veldra Body Care</tspan>
    <tspan x="1117" dy="17">27 Maple Row, Suite 4</tspan>
    <tspan x="1117" dy="17">Lakeview ON, L2X 3B9 Canada</tspan>
  </text>
  <path class="board" d="M998 1205 H1235 V1285 Q1235 1335 1185 1335 H1048 Q998 1335 998 1285 Z"/>
  <path class="crease" d="M1003 1215 H1060 V1200 H1172 V1215 H1230 V1280 Q1230 1330 1183 1330 H1050 Q1003 1330 1003 1280 Z"/>
</svg>
</body>
</html>
```